We need (2) 4"X4" product label designs for the front and back of an RTU hose on bottle (see attached examples) for a brand new, first-of-its-kind, Aloe Vera product (VerdaKin "The Supreme Root Tonic") specially formulated for agriculture. Most people are aware of the medicinal benefits of aloe vera, however, most people are unaware that it can be used as a soil amendment (organic fertilizer) for plants and lawns, as well as many other crops. This product is for the consumer market. There are about 15 elements that need to go on the front label (which I will provide moving forward), and the backside provides instructions and other relevant information about the product. I will provide a range of examples on the next step of this project.

Need extra days to review

```html
<!DOCTYPE html>
<html lang="en">
<head>
<meta charset="utf-8">
<title>VerdaKin – The Supreme Root Tonic – Front Label</title>
<link rel="stylesheet" href="https://fonts.googleapis.com/css2?family=Oswald:wght@500;700&family=Poppins:ital,wght@0,400;0,600;0,700;1,800&display=swap">
<style>
  :root {
    --page: #ffffff;
    --green-dark: #0f6840;
    --green-mid: #4f9c45;
    --green-light: #7cbb4b;
    --accent-red: #ec1c24;
    --accent-yellow: #fff200;
    --navy: #2b3192;
    --ink: #1d1d1b;
    --white: #ffffff;
  }
  * { margin: 0; padding: 0; box-sizing: border-box; }
  html, body {
    width: 1200px;
    height: 1200px;
    overflow: hidden;
    background: var(--page);
  }
  .label {
    position: absolute;
    left: 100px;
    top: 100px;
    width: 1000px;
    height: 1000px;
    overflow: hidden;
    background: linear-gradient(35deg, var(--green-dark) 0%, var(--green-mid) 50%, var(--green-light) 100%);
    font-family: "Poppins", sans-serif;
    color: var(--white);
  }
  .corner-new {
    position: absolute;
    left: -290px;
    top: -290px;
    width: 580px;
    height: 580px;
    border-radius: 50%;
    background: var(--accent-red);
  }
  .corner-new__text {
    position: absolute;
    left: 93px;
    top: 96px;
    font-family: "Oswald", sans-serif;
    font-weight: 700;
    font-size: 68px;
    line-height: 1;
    color: var(--accent-yellow);
  }
  .corner-facts {
    position: absolute;
    right: -300px;
    top: -300px;
    width: 600px;
    height: 600px;
    border-radius: 50%;
    background: var(--accent-yellow);
  }
  .corner-facts__text {
    position: absolute;
    right: 88px;
    top: 96px;
    font-family: "Oswald", sans-serif;
    font-weight: 500;
    font-size: 24px;
    line-height: 46px;
    color: var(--ink);
    text-align: right;
  }
  .brand {
    position: absolute;
    left: 0;
    top: 96px;
    width: 1000px;
    height: 240px;
  }
  .brand__disc {
    position: absolute;
    left: 387px;
    top: 0;
    width: 240px;
    height: 240px;
    border-radius: 50%;
    background: var(--navy);
  }
  .brand__name {
    position: absolute;
    left: 0;
    width: 1000px;
    top: 80px;
    text-align: center;
    font-weight: 700;
    font-size: 64px;
    line-height: 80px;
    color: var(--white);
  }
  .headline {
    position: absolute;
    left: 0;
    width: 1000px;
    top: 378px;
    text-align: center;
    font-weight: 800;
    font-style: italic;
    font-size: 88px;
    line-height: 100px;
    letter-spacing: -1px;
  }
  .use-tag {
    position: absolute;
    left: 136px;
    top: 606px;
    width: 746px;
    height: 114px;
    background: var(--accent-red);
    border-radius: 50px;
    transform: skewX(-14deg);
  }
  .use-tag__text {
    position: absolute;
    left: 0;
    width: 1000px;
    top: 606px;
    height: 114px;
    line-height: 114px;
    text-align: center;
    font-weight: 700;
    font-size: 68px;
    color: var(--accent-yellow);
  }
  .details-title {
    position: absolute;
    left: 0;
    width: 1000px;
    top: 750px;
    text-align: center;
    font-weight: 600;
    font-size: 34px;
    letter-spacing: 9px;
  }
  .details-copy {
    position: absolute;
    left: 85px;
    width: 830px;
    top: 828px;
    text-align: center;
    font-weight: 400;
    font-size: 15.5px;
    line-height: 21px;
    text-transform: uppercase;
  }
</style>
</head>
<body>
  <main class="label" aria-label="VerdaKin front label">
    <div class="corner-new"></div>
    <span class="corner-new__text">NEW</span>

    <div class="corner-facts"></div>
    <p class="corner-facts__text">100% NATURAL<br>1400ML</p>

    <div class="brand">
      <div class="brand__disc"></div>
      <p class="brand__name">VerdaKin</p>
    </div>

    <h1 class="headline">The Supreme<br>Root Tonic</h1>

    <div class="use-tag"></div>
    <p class="use-tag__text">FOR AGRICULTURE</p>

    <h2 class="details-title">LABEL DETAILS</h2>
    <p class="details-copy">Lorem ipsum dolor sit amet, consectetuer adipiscing elit, sed diam nonummy nibh euismod tincidunt ut laoreet dolore magna aliquam erat volutpat. Ut wisi enim ad minim veniam, quis nostrud exerci tation ullamcorper suscipit lobortis nisl ut aliquip ex ea commodo consequat. Duis autem vel eum iriure dolor in hendrerit</p>
  </main>
</body>
</html>
```